PowerPoint Design Project

We've recently updated our logo and we are in the processing of updating our web sites, business cards, letterhead, etc.

We're looking for a complete redesign of our Powerpoint template, which we have attached for reference.

Unfortunately our new web site is not released and is currently undergoing redesign so we can't send you a link to inspire.

Also attached here is our new logo.

Target Market(s)

Executives, Ph.D. scientists, researchers, venture capitalists, Board members

Industry/Entity Type

Business

```html
<!DOCTYPE html>
<html lang="en">
<head>
<meta charset="utf-8">
<title>HelixTrail – Presentation Template</title>
<link href="https://fonts.googleapis.com/css2?family=Montserrat:wght@600&family=Arimo:wght@400&display=swap" rel="stylesheet">
<style>
  :root {
    --stage: #141414;
    --slide: #ffffff;
    --brand-blue: #2a93c8;
    --ink: #333333;
  }
  html, body {
    margin: 0;
    padding: 0;
    width: 1200px;
    height: 1000px;
    overflow: hidden;
    background: var(--stage);
  }
  .slide {
    position: absolute;
    left: 91px;
    top: 140px;
    width: 1018px;
    height: 720px;
    background: var(--slide);
  }
  .brand {
    position: absolute;
    left: 44px;
    top: 40px;
    display: flex;
    align-items: center;
    gap: 10px;
  }
  .brand-dot {
    width: 48px;
    height: 48px;
    border-radius: 50%;
    background: var(--brand-blue);
  }
  .brand-name {
    font-family: "Montserrat", sans-serif;
    font-weight: 600;
    font-size: 37px;
    letter-spacing: -0.5px;
    color: var(--brand-blue);
    line-height: 1;
  }
  .rule {
    position: absolute;
    background: var(--brand-blue);
    border-radius: 3px;
  }
  .rule-header {
    left: 37px;
    top: 109px;
    width: 875px;
    height: 6px;
  }
  .rule-footer {
    left: 42px;
    top: 655px;
    width: 860px;
    height: 5px;
  }
  .tagline {
    position: absolute;
    left: 47px;
    top: 672px;
    margin: 0;
    font-family: "Arimo", sans-serif;
    font-size: 15px;
    letter-spacing: 0.15px;
    line-height: 20px;
    color: var(--ink);
  }
  .corner-mark {
    position: absolute;
    left: 884px;
    top: 566px;
    width: 114px;
    height: 114px;
    border-radius: 50%;
    background: var(--brand-blue);
  }
</style>
</head>
<body>
  <main class="slide">
    <header class="brand">
      <span class="brand-dot"></span>
      <span class="brand-name">HelixTrail</span>
    </header>
    <div class="rule rule-header"></div>

    <footer>
      <div class="rule rule-footer"></div>
      <p class="tagline">Search, manage, mine and share the world´s sequence data</p>
      <div class="corner-mark"></div>
    </footer>
  </main>
</body>
</html>
```